New Poster Design Project

Make an out standing A2 poster with below information,it is out first edition!Use the Attached image as background,Thanx!

Tolvik Meridian Arts Gathering
16 - 22 June 2014
Www.tmagfest.example

Creating a new vision of Africa through African Arts and Culture

Guest speakers / Artists

Delphine Korrato-Væstrup (S.A)
Tekle Berhanu Woldesan (Ethio)
Ronny Bastien-Kolo (Uganda)
Håkon Lunde (Nor)
Velvet Drum Collective (Zim)
Kalumbero Band (Moz,Nor,Swe & Zim)
Dj Zoto Zoto with Afro beats (Ghana/UK )
Dj Marquee/Storm Duchess with collage mix (Bergen)

@ Cafe Lutembe, Nordvik Global Heritage House (Nghh) Helsebrygga,Kjøpmannsplassen,Lindehagen & Vevergangen gate

Mon-Thur
Free entry,food & drinks served

Fri - Entry by donation & Sat - Tmagfest closing ceremony (100kr)
Updates

Project Deadline Extended

Project Deadline Extended
Reason: I made a mistake on extending time on this project now I can not reverse the extended time aaarrrr!!!I really dont have time,The poster should be all over the place by now since Im left with a couple of days away to the festival!!!I need someone to QuickFix me a A2 top notch poster in No time...my deadline is NOW NOW,LATEST Wednesday 21 May 2014,Thanx!

Industry/Entity Type

Cafe

Requirements
Must have
• sponsors logo
Nice to have
• Symbols
Should not have

```html
<!DOCTYPE html>
<html lang="en">
<head>
<meta charset="utf-8">
<title>TMAG – Tolvik Meridian Arts Gathering 2014</title>
<link href="https://fonts.googleapis.com/css2?family=Josefin+Sans:wght@100;300&family=Roboto:wght@300;400;500&display=swap" rel="stylesheet">
<style>
  :root {
    --paper: #ffffff;
    --night: #1c1611;
    --night-soft: #2b221b;
    --sepia-light: #b59a80;
    --sepia-mid: #7a5f48;
    --sepia-dark: #2e231a;
    --sky: #7f9fba;
    --ink: #2a2a2a;
    --grey: #8a8a8a;
    --sun: #e9e47c;
    --rust: #c0542a;
    --rust-soft: #9c4a2a;
    --sand: #f0d8b8;
    --white: #ffffff;
  }
  html, body { margin: 0; padding: 0; overflow: hidden; background: var(--paper); }
  .poster {
    position: relative; width: 849px; height: 1200px; overflow: hidden;
    background: var(--paper); font-family: "Roboto", Arial, sans-serif;
  }
  .dark-field {
    position: absolute; left: 0; top: 188px; width: 849px; height: 893px;
    background: linear-gradient(90deg, var(--night) 0%, var(--night-soft) 60%, var(--sepia-dark) 100%);
  }
  .portrait {
    position: absolute; left: 390px; top: 0; width: 459px; height: 1081px;
    background: radial-gradient(ellipse at 55% 45%, var(--sepia-light) 0%, var(--sepia-mid) 45%, rgba(46,35,26,0) 85%);
  }
  .site-url {
    position: absolute; left: 82px; top: 46px; font-family: "Josefin Sans", sans-serif;
    font-weight: 300; font-size: 20px; letter-spacing: 5px; color: var(--grey);
  }
  .festival-mark {
    position: absolute; left: 80px; top: 112px; font-family: "Josefin Sans", sans-serif;
    font-weight: 100; font-size: 72px; letter-spacing: 30px; color: var(--ink); line-height: 1;
  }
  .symbol-row { position: absolute; left: 92px; top: 210px; display: flex; gap: 30px; }
  .symbol { width: 38px; height: 48px; }
  .symbol--sun { background: var(--sun); }
  .symbol--rust { background: var(--rust); }
  .symbol--sky { background: var(--sky); }
  .symbol--sand { background: var(--sand); }
  .name-band {
    position: absolute; left: 0; top: 292px; width: 440px; height: 26px; background: var(--sky);
    font-size: 12px; letter-spacing: 3px; line-height: 26px; padding-left: 74px; box-sizing: border-box;
    color: var(--ink); white-space: nowrap;
  }
  .name-band .soft { color: #c9d6e2; }
  .dates {
    position: absolute; left: 74px; top: 338px; font-family: "Josefin Sans", sans-serif; font-weight: 300;
    font-size: 38px; color: var(--sun);
  }
  .mission {
    position: absolute; left: 74px; top: 392px; width: 420px; margin: 0; font-weight: 400;
    font-size: 30px; line-height: 36px; color: var(--white);
  }
  .lineup { position: absolute; left: 68px; top: 511px; margin: 0; padding: 0; list-style: none; }
  .lineup li {
    display: table; background: var(--rust-soft); color: var(--sand); font-size: 13.5px;
    line-height: 18.5px; padding: 0 6px; margin: 0;
  }
  .lineup li.lineup-title { background: var(--rust); color: var(--white); font-size: 16px; line-height: 20px; }
  .venue { position: absolute; left: 74px; top: 682px; color: var(--white); }
  .venue-name { font-size: 30px; margin: 0 0 6px; font-weight: 400; }
  .venue-address { font-size: 12.5px; line-height: 16px; margin: 0; }
  .schedule { position: absolute; left: 74px; top: 776px; color: var(--sun); }
  .schedule dt { font-size: 18px; margin-top: 10px; }
  .schedule dd { font-size: 12.5px; margin: 2px 0 0; }
  .rule { position: absolute; left: 0; top: 1081px; width: 849px; height: 9px; background: var(--rust-soft); }
  .sponsors {
    position: absolute; left: 0; top: 1090px; width: 849px; height: 110px; display: flex;
    align-items: center; justify-content: space-around; padding: 0 80px; box-sizing: border-box;
  }
  .sponsor { display: flex; align-items: center; gap: 5px; font-size: 11px; font-weight: 500; color: var(--ink); }
  .sponsor .dot { width: 22px; height: 22px; border-radius: 50%; background: var(--rust); }
</style>
</head>
<body>
<main class="poster">
  <div class="dark-field"></div>
  <div class="portrait" role="img" aria-label="Sepia portrait of a smiling woman in a white head wrap, seated and holding a thumb piano in a decorated gourd"></div>

  <div class="site-url">www.tmagfest.example</div>
  <div class="festival-mark">TMAG</div>

  <div class="symbol-row" role="img" aria-label="Row of four traditional African symbols">
    <div class="symbol symbol--sun"></div>
    <div class="symbol symbol--rust"></div>
    <div class="symbol symbol--sky"></div>
    <div class="symbol symbol--sand"></div>
  </div>

  <div class="name-band">Tolvik <span class="soft">Meridian</span> Arts <span class="soft">Gathering</span></div>

  <div class="dates">16-22 June 2014</div>
  <h1 class="mission">Creating a new vision of Africa through African Arts and Culture</h1>

  <ul class="lineup">
    <li class="lineup-title">Guest speakers / Artists</li>
    <li>Delphine Korrato-Væstrup (S.A)</li>
    <li>Tekle Berhanu Woldesan (Ethio)</li>
    <li>Ronny Bastien-Kolo (Uganda)</li>
    <li>Håkon Lunde (Nor)</li>
    <li>Velvet Drum Collective (Zim)</li>
    <li>Kalumbero Band (Moz,Nor,Swe &amp; Zim)</li>
    <li>Dj Zoto Zoto with Afro beats (Ghana/UK )</li>
    <li>Dj Marquee/Storm Duchess with collage mix (Bergen)</li>
  </ul>

  <div class="venue">
    <p class="venue-name">@ Cafe Lutembe,</p>
    <p class="venue-address">Nordvik Global Heritage House (Nghh)<br>Helsebrygga, Kjøpmannsplassen,<br>Lindehagen &amp; Vevergangen gate</p>
  </div>

  <dl class="schedule">
    <dt>Monday - Thursday</dt><dd>Free entry, food &amp; drinks served</dd>
    <dt>Friday</dt><dd>Entry by donation</dd>
    <dt>Saturday</dt><dd>Tmagfest closing ceremony (100kr)</dd>
  </dl>

  <div class="rule"></div>
  <footer class="sponsors">
    <div class="sponsor"><span class="dot"></span>Nordvik Heritage</div>
    <div class="sponsor">lyktehuset.example</div>
    <div class="sponsor">fkru.example</div>
    <div class="sponsor">Tolvik Kommune</div>
    <div class="sponsor">Kora Step Ensemble</div>
    <div class="sponsor">Dugnad Hub</div>
  </footer>
</main>
</body>
</html>
```